Gerald Pinnock - Corporate MC & Entertainer

Design a one page A4 flyer
(See Brief Attached)
I'm after a one Page Flyer
A4 Size - One sided
I want the finished artwork in 2 Forms.
1/ One that I could print out myself in a small run ( I have a Dorvan Tint PrintMaster)
or send out as a PDF
2/ A second version that could be printed commercially , so including bleed crop marks so it can be cut to A4 size
I have attached the copy that should be included. (Agency Sweep 2014 WORDS)
If there was too much text to include , we could drop one of the testimonial quotes
I have attached 3 images that could be included if there is room.
If there were too many images I suggest dropping Image 3 ( with bow tie)
As you can see from the copy (or a visit to my website) there are two main services that I provide
Corporate MC Services and Entertainment Services.
These are however intertwined - My MC work often includes some entertaining effects from my ThoughtCatcher Show. I often get booked to MC a conference and provide a show.
I'm after something that is -
Classy , Sophisticated, Smart, perhaps a bit quirky.
Nothing "Magic" like - eg no Rabbits , Wands, puffs of smoke
I have no corporate colour or logo or branding that should be included
You can see some previous flyers here http://www.proflinkora.com/in/geraldpinnock
I like these, but looking for new ideas
Target Market(s)
Corporate , Conference Organisers, Speaker Bureau owners, Large Association Conference committees
Industry/Entity Type
Entertainment
Colors
Designer to choose colors to be used in the design.

```html
<!DOCTYPE html>
<html lang="en">
<head>
<meta charset="utf-8">
<title>Gerald Pinnock – Corporate MC &amp; Entertainer</title>
<link href="https://fonts.googleapis.com/css2?family=Anton&family=Francois+One&family=Jost:wght@400;600&family=PT+Sans+Narrow:wght@700&display=swap" rel="stylesheet">
<style>
  :root {
    --night: #050507;
    --night-glow: #141826;
    --cream: #f4efc8;
    --yellow: #f3e600;
    --band: #f0e000;
    --orange: #e2782c;
    --white: #ffffff;
    --ink: #111111;
  }
  html, body {
    margin: 0;
    padding: 0;
    width: 812px;
    height: 1200px;
    overflow: hidden;
    background: var(--night);
  }
  .flyer {
    position: relative;
    width: 812px;
    height: 1200px;
    background: radial-gradient(ellipse at 50% 55%, var(--night-glow) 0%, var(--night) 70%);
    color: var(--white);
    text-align: center;
    overflow: hidden;
  }
  .starfield {
    position: absolute;
    inset: 0;
    background: radial-gradient(circle at 50% 50%, rgba(120,140,200,0.10), rgba(0,0,0,0) 65%);
  }
  .name {
    position: absolute;
    top: 18px;
    left: 0;
    width: 100%;
    margin: 0;
    font-family: "Francois One", sans-serif;
    font-size: 112px;
    line-height: 1;
    color: var(--cream);
    letter-spacing: 1px;
  }
  .tagline {
    position: absolute;
    top: 150px;
    left: 0;
    width: 100%;
    margin: 0;
    font-family: "Anton", sans-serif;
    font-size: 42px;
    color: var(--yellow);
    letter-spacing: 0.5px;
  }
  .role {
    position: absolute;
    top: 212px;
    left: 0;
    width: 100%;
    margin: 0;
    font-family: "Jost", sans-serif;
    font-weight: 400;
    font-size: 34px;
    color: var(--white);
  }
  .hook {
    position: absolute;
    top: 258px;
    left: 0;
    width: 100%;
    margin: 0;
    font-family: "Jost", sans-serif;
    font-weight: 600;
    font-size: 38px;
    color: var(--orange);
  }
  .bio {
    position: absolute;
    top: 322px;
    left: 70px;
    width: 672px;
    font-family: "PT Sans Narrow", sans-serif;
    font-weight: 700;
    font-size: 21px;
    line-height: 1.18;
  }
  .bio p { margin: 0 0 22px; }
  .portrait {
    position: absolute;
    left: 140px;
    top: 690px;
    width: 520px;
    height: 400px;
    background: linear-gradient(180deg, #1d2350 0%, #232a6a 55%, #151a3e 100%);
    border-radius: 4px;
  }
  .testimonials {
    position: absolute;
    top: 650px;
    left: 500px;
    width: 260px;
    text-align: left;
    font-family: "Jost", sans-serif;
    z-index: 2;
  }
  .testimonials h2 {
    margin: 0 0 4px;
    font-size: 17px;
    font-weight: 600;
  }
  .quote {
    margin: 0;
    font-size: 15px;
    line-height: 1.3;
  }
  .quote .mark { color: var(--yellow); font-weight: 600; font-size: 22px; line-height: 0; }
  .quote-source {
    margin: 8px 0 0;
    text-align: right;
    font-size: 13px;
    padding-right: 20px;
  }
  .upcoming {
    position: absolute;
    top: 1060px;
    left: 160px;
    margin: 0;
    font-family: "Jost", sans-serif;
    font-weight: 600;
    font-size: 26px;
    color: var(--yellow);
    z-index: 2;
  }
  .cta-band {
    position: absolute;
    left: 0;
    bottom: 0;
    width: 100%;
    height: 96px;
    background: var(--band);
    display: flex;
    align-items: center;
    justify-content: center;
    font-family: "Jost", sans-serif;
    font-weight: 400;
    font-size: 30px;
    color: var(--ink);
  }
  .cta-band .url { margin-left: 26px; }
</style>
</head>
<body>
  <main class="flyer">
    <div class="starfield" role="img" aria-label="Starry night sky backdrop"></div>

    <h1 class="name">Gerald Pinnock</h1>
    <p class="tagline">"Australia's Magician of the Mind"</p>
    <p class="role">Corporate MC &amp; Entertainer</p>
    <p class="hook">Solving your Conference Puzzles!</p>

    <section class="bio">
      <p>In the last two years Gerald has been engaged as the Conference MC for events in Hawaii, New Zealand, Hong Kong &amp; all States of Australia. He facilitated 24 Australian Major Project Conferences for ExpoMeridian and 16 International CEO Summits for Halvorn Global.</p>
      <p>In the Australian Corporate Sector, he managed major events for OzLedger Brokers, NRBA, Carewell, Sound Hire Co, Harbourside Care and the Growers &amp; Garden Guild.</p>
      <p>As an Entertainer he cruised the world on several luxury cruise ships, visiting Japan, Korea, China, Tahiti and New Zealand in his travels.</p>
    </section>

    <div class="portrait" role="img" aria-label="Photo of Gerald Pinnock on stage in a blue suit at a microphone, arms spread wide"></div>

    <aside class="testimonials">
      <h2>Recent Testimonials</h2>
      <p class="quote"><span class="mark">&ldquo;</span> Huge thanks for your professionalism with the Awards, getting a laugh from everyone and in general creating an atmosphere that was enjoyable and relaxed!<span class="mark">&rdquo;</span></p>
      <p class="quote-source">- Carewell</p>
    </aside>

    <p class="upcoming">What's coming up in 2014?</p>
    <footer class="cta-band">
      <span>Get involved at</span><span class="url">http://www.GeraldPinnock.com</span>
    </footer>
  </main>
</body>
</html>
```